Paraffin Wax Packaging Design for Nail and Beauty Industry

We need an attractive design for the packaging of our new product, Paraffin Wax. Our company is a wholesale beauty/nail supply company that has been selling to nail salons in the US market for 10 years. We currently sell this product that we buy from another company. Now we want to launch our own brand of Paraffin Wax.

Target Market(s)

Retail nail salons in the US market.

Industry/Entity Type

Industry

Font styles to use
Sans Serif

Colors

Designer to choose colors to be used in the design.

Requirements
Must have
• Our logo (attached).
• All information on the "Ingredient List" (attached).
• Design for Clear Packaging so product can show through.
• Design for Package Dimensions of 4.25" x 11" (110cm x 280 cm).
Nice to have
• Picture related to women's skin and or beauty.
• Contrast as in the design of product that we currently sell (attached).

```html
<!DOCTYPE html>
<html lang="en">
<head>
<meta charset="utf-8">
<title>Paraffin Wax Pack Front</title>
<link href="https://fonts.googleapis.com/css2?family=Oswald:wght@600&family=Open+Sans:wght@400;700&display=swap" rel="stylesheet">
<style>
  :root {
    --page: #ffffff;
    --wax: #8e4fd6;
    --wax-deep: #7a3cc4;
    --wax-edge: #9aa893;
    --band-light: #ffffff;
    --ink: #1a1a1a;
    --ink-soft: #2e2e2e;
    --brand-ink: #1f2a4d;
    --skin-light: #f1e6df;
    --skin-mid: #d9b8a3;
  }
  * { margin: 0; padding: 0; box-sizing: border-box; }
  html, body { width: 676px; height: 1200px; overflow: hidden; background: var(--page); }
  .canvas { position: relative; width: 676px; height: 1200px; }

  .pack {
    position: absolute; left: 75px; top: 45px; width: 525px; height: 1105px;
    background: var(--wax-edge);
  }
  .wax-top, .wax-bottom {
    position: absolute; left: 22px; right: 22px;
    background: linear-gradient(180deg, var(--wax) 0%, var(--wax-deep) 100%);
  }
  .wax-top { top: 10px; height: 290px; }
  .wax-bottom { top: 770px; height: 315px; }

  .brand {
    position: absolute; left: 0; right: 0; top: 150px;
    text-align: center;
    font-family: "Open Sans", sans-serif; font-weight: 700;
    font-size: 42px; color: var(--brand-ink); letter-spacing: 0.5px;
  }
  .brand-tag {
    display: block; font-size: 12px; margin-top: 2px; margin-left: 170px;
  }

  .hero {
    position: absolute; left: 0; right: 0; top: 290px; height: 480px;
    background: linear-gradient(135deg, var(--band-light) 0%, var(--skin-light) 45%, var(--skin-mid) 70%, var(--band-light) 100%);
  }
  .product-name {
    position: absolute; left: 123px; top: 395px;
    font-family: "Oswald", sans-serif; font-weight: 600;
    font-size: 46px; line-height: 1; color: var(--ink); letter-spacing: 0.5px;
  }
  .product-note {
    position: absolute; right: 60px; top: 452px; width: 300px;
    text-align: right;
    font-family: "Open Sans", sans-serif; font-size: 16px; line-height: 1.3;
    color: var(--ink-soft);
  }

  .info {
    position: absolute; left: 68px; right: 40px; top: 812px;
    font-family: "Open Sans", sans-serif; font-size: 14.5px; line-height: 1.45;
    color: var(--ink-soft);
  }
  .info p + p { margin-top: 10px; }
  .info strong { color: var(--ink); }
  .net-weight {
    position: absolute; left: 0; right: 0; top: 1003px; text-align: center;
    font-family: "Open Sans", sans-serif; font-size: 20px; color: var(--ink-soft);
  }
</style>
</head>
<body>
<div class="canvas">
  <div class="pack">
    <div class="wax-top"></div>
    <div class="wax-bottom"></div>

    <div class="brand">By Lorava<span class="brand-tag">Glow Daily</span></div>

    <div class="hero" role="img" aria-label="Photo of a seated woman's smooth bare legs with a pink lily, on a white background"></div>

    <h1 class="product-name">PARAFFIN WAX</h1>
    <p class="product-note">Compatible for use with most wax paraffin heat therapy units</p>

    <div class="info">
      <p><strong>Ingredients:</strong> Paraffin waxes and Hydrocarbon waxes, Petrolatum, Paraffin oils, Apricot kernel oil, Fragrance D &amp; C dyes.</p>
      <p><strong>Caution:</strong> Paraffin is flammable.<br>Do not use near open flame or an unprotected resistance heater.</p>
    </div>

    <p class="net-weight">Net Wt. 1 lb. (450 g.)</p>
  </div>
</div>
</body>
</html>
```